Creative Stationary for Solo Law Firm

I am looking for stationary designs for my solo law firm called TM Halvorsen Law PLLC. My logo is attached. I'd like the logo incorporated into the design.

I'm looking for a stationary design that is a bit outside of the box and not too standard or boring. The final design should communicate professionalism.

Target Market(s)

United States Clients, Opposing Counsel

Industry/Entity Type

Legal

Font styles to use
Sans Serif

Requirements
Must have
• The stationary design must incorporate my logo design attached. The design itself must be creative. The envelope design must follow standard United States designs with room for the postage stamp at the top right corner and space for the recipient's address in the middle.

```html
<!DOCTYPE html>
<html lang="en">
<head>
<meta charset="utf-8">
<title>TM Halvorsen Law — Stationery</title>
<link href="https://fonts.googleapis.com/css2?family=Cinzel:wght@400&family=Open+Sans:wght@400&display=swap" rel="stylesheet">
<style>
  :root {
    --backdrop: #939393;
    --paper: #ffffff;
    --navy: #1c1f5c;
    --ink: #222222;
    --flap-line: #555555;
  }
  * { margin: 0; padding: 0; box-sizing: border-box; }
  html, body { width: 1200px; height: 960px; overflow: hidden; }
  body { background: var(--backdrop); position: relative; font-family: "Open Sans", Arial, sans-serif; }

  .sheet { position: absolute; background: var(--paper); }

  .letterhead { left: 58px; top: 144px; width: 520px; height: 673px; }
  .letterhead .firm-name {
    position: absolute; top: 48px; left: 0; width: 100%;
    text-align: center; font-family: "Cinzel", Georgia, serif;
    font-size: 20px; color: var(--navy); letter-spacing: 0.3px;
  }
  .letterhead .contact-bar {
    position: absolute; top: 645px; left: 60px; width: 400px;
    display: flex; align-items: center; justify-content: space-between;
    font-size: 6.2px; line-height: 8px; color: var(--ink); white-space: nowrap;
  }
  .contact-item { display: flex; align-items: center; gap: 3px; }
  .contact-item svg { width: 6px; height: 6px; flex: none; }
  .contact-address { color: var(--navy); border-left: 1px solid var(--navy); padding-left: 5px; }

  .envelope-front { left: 614px; top: 190px; width: 550px; height: 247px; }
  .envelope-front .firm-name {
    position: absolute; top: 21px; left: 19px;
    font-family: "Cinzel", Georgia, serif; font-size: 12px; color: var(--navy);
  }
  .envelope-front .return-address {
    position: absolute; top: 45px; left: 19px;
    font-size: 7px; line-height: 8.5px; color: var(--ink);
  }

  .envelope-back { left: 614px; top: 504px; width: 550px; height: 246px; }
  .envelope-back svg { position: absolute; left: 0; top: 0; }
</style>
</head>
<body>

<section class="sheet letterhead">
  <div class="firm-name">TM Halvorsen Law</div>
  <div class="contact-bar">
    <span class="contact-item">
      <svg viewBox="0 0 10 10"><path d="M2 1 L4 1 L4.6 3.2 L3.4 4 Q4.4 6 6 6.6 L6.8 5.4 L9 6 L9 8 Q5 9.5 1 2 Z" fill="var(--navy)"/></svg>
      +1 555 014 2287
    </span>
    <span class="contact-item">
      <svg viewBox="0 0 10 10"><rect x="0.5" y="2" width="9" height="6" fill="var(--navy)"/><path d="M0.5 2 L5 5.5 L9.5 2" stroke="#fff" stroke-width="0.8" fill="none"/></svg>
      info@halvorsenlaw.com
    </span>
    <span class="contact-item">
      <svg viewBox="0 0 10 10"><circle cx="5" cy="5" r="4.2" fill="none" stroke="var(--navy)" stroke-width="1"/><path d="M1 5 H9 M5 1 V9" stroke="var(--navy)" stroke-width="0.8"/></svg>
      www.halvorsenlaw.com
    </span>
    <span class="contact-address">4820 Marlow Ave, Suite 210, Larkfield, City 90412</span>
  </div>
</section>

<section class="sheet envelope-front">
  <div class="firm-name">TM Halvorsen Law</div>
  <div class="return-address">
    4820 Marlow Ave, Suite 210<br>
    Larkfield, City 90412
  </div>
</section>

<section class="sheet envelope-back">
  <svg width="550" height="246" viewBox="0 0 550 246">
    <path d="M0 0 L3 64 Q4 72 14 72 L240 71 Q275 70 310 71 L536 72 Q546 72 547 64 L550 0"
          fill="none" stroke="var(--flap-line)" stroke-width="1"/>
  </svg>
</section>

</body>
</html>
```